Consulting/Brand Licensing business needs business card

We need a business card created for our IP company, that also does consulting and brand licensing. We would like this card to be vague, as our other business' are in the cannabis industry and this is a non-cannabis touching entity. Perhaps something that hints vaguely at the industry without alerting or possibly offending the receiver.

Target Market(s)

CEOs/Key Decision Makers/Industry Leaders

Contact Information for Business Card

No address, simply list Seattle, WA. Phone: 206-555-0147. Name: Dilan Vesterby // email: Dilan@pulvanixa.com

Colors

Designer to choose colors to be used in the design.

Requirements
Must have
• Logo, Name, Email, Phone number, "Consulting, Licensing and Branding Specialists"
Nice to have
• We would like this to be more professional than playful.

```html
<!DOCTYPE html>
<html lang="en">
<head>
<meta charset="utf-8">
<title>Pulvanixa, Inc — Business Card</title>
<link rel="stylesheet" href="https://fonts.googleapis.com/css2?family=Didact+Gothic&family=Montserrat:wght@700&display=swap">
<style>
  :root {
    --page-bg: #ecebe8;
    --brand-orange: #e04a2b;
    --card-white: #f7f7f6;
    --ink-white: #ffffff;
    --rule-white: rgba(255, 255, 255, 0.75);
    --ink-grey: #3a3a3a;
  }
  * { margin: 0; padding: 0; box-sizing: border-box; }
  html, body {
    width: 1200px;
    height: 911px;
    overflow: hidden;
    background: var(--page-bg);
  }
  .sheet {
    width: 1200px;
    height: 911px;
    display: flex;
    align-items: center;
    justify-content: center;
    gap: 60px;
  }
  .card {
    width: 525px;
    height: 300px;
    position: relative;
    box-shadow: 0 10px 24px rgba(0, 0, 0, 0.18);
  }
  .card--contact {
    background: var(--brand-orange);
    color: var(--ink-white);
  }
  .contact-block {
    position: absolute;
    left: 238px;
    top: 84px;
    font-family: "Didact Gothic", "Century Gothic", sans-serif;
    font-size: 15px;
    line-height: 1.55;
  }
  .contact-name {
    font-family: "Montserrat", "Century Gothic", sans-serif;
    font-weight: 700;
    font-size: 19px;
    margin-bottom: 2px;
    letter-spacing: -0.2px;
  }
  .contact-line--ruled {
    border-bottom: 1px solid var(--rule-white);
    padding-bottom: 4px;
    margin-bottom: 6px;
    width: 190px;
  }
  .card--logo {
    background: var(--card-white);
    display: flex;
    align-items: center;
    justify-content: center;
  }
  .brand-name {
    font-family: "Didact Gothic", "Century Gothic", sans-serif;
    font-size: 44px;
    color: var(--brand-orange);
    letter-spacing: 1px;
  }
</style>
</head>
<body>
  <main class="sheet">
    <section class="card card--contact" aria-label="Card back with contact details">
      <div class="contact-block">
        <p class="contact-name">Dilan Vesterby</p>
        <p class="contact-line">Seattle, WA.</p>
        <p class="contact-line">(P) 206-555-0147</p>
        <p class="contact-line contact-line--ruled">Dilan@pulvanixa.com</p>
        <p class="contact-line contact-line--ruled">www.pulvanixa.com</p>
      </div>
    </section>
    <section class="card card--logo" aria-label="Card front with company name">
      <p class="brand-name">Pulvanixa, Inc</p>
    </section>
  </main>
</body>
</html>
```